Boutique Jewellery Card [UPDATED] Embossing and Foil

Hi Designers,

What will win you this competition is your input on making my card look very professional and classy

Just some overview information.

I am striving to be the most prestigious jeweller going around specialising in custom designed jewellery, engagement rings and repairs on a bigger budget.

I am spending a lot on the printing including thick cards, rounded corners, multi level embossing and foiling.

Front:

I want my entire logo on the front, which I will have embossed and foiled (source file included)
Optional: I also want a lower embossing of a repeating pattern which I am not sure on. I need YOUR input here

Back:

I need you to use your skills and experience to make my details look very important, professional and classy.

The details I need on the back are:

Marcus Feldwright
Your Jewellery Stylist

www.marcusfeldwright.com
0492 836 514
marcus@marcusfeldwright.com

The font MUST match the font/style used in the logo.
Everything else including layout, whether my logo is on the back etc, engrave/endent, foiling etc is what I need your input for
Updates

Project Deadline Extended Reason: I was a bit slow and out of action at the start, but we're almost there, just need a few more days to finalize Added Sunday, November 16, 2014

Target Market(s)

25 - 80 year olds. Fashion concious. Wealthy

Industry/Entity Type

Printing

Contact Information for Business Card

Marcus Feldwright
Your Jewellery Stylist

0492 836 514
marcus@marcusfeldwright.com
www.marcusfeldwright.com
- facebook and instagram logo's

Requirements
Must have
• Must use the font from my logo on the back, or very similar
• My logo on the front
• My details on the back must be the centre of attention, my logo can still be there but is less important.
• Back must include the facebook and instagram logo's
Nice to have
• repeating pattern or monogram

```html
<!DOCTYPE html>
<html lang="en">
<head>
<meta charset="utf-8">
<title>Marcus Feldwright – Business Card</title>
<link href="https://fonts.googleapis.com/css2?family=Raleway:wght@300;400&family=Open+Sans:wght@400;600;700&display=swap" rel="stylesheet">
<style>
  :root {
    --backdrop: #e6e3de;
    --band-dark: #1b1b1b;
    --band-mid: #2b2b2b;
    --panel: #dcd7cf;
    --panel-light: #ece8e2;
    --silver-1: #f4f4f4;
    --silver-2: #9a9a9a;
    --silver-3: #5e5e5e;
    --ink: #2e2e2e;
    --ink-soft: #555;
    --logo-grey: #c9c9c9;
    --white: #ffffff;
  }
  * { box-sizing: border-box; margin: 0; padding: 0; }
  html, body { width: 1149px; height: 1200px; overflow: hidden; }
  body { background: var(--backdrop); position: relative; font-family: "Open Sans", sans-serif; }

  .card {
    position: absolute; left: 184px; width: 781px;
    padding: 5px;
    background: linear-gradient(135deg, var(--silver-1), var(--silver-2) 30%, var(--silver-1) 55%, var(--silver-3) 80%, var(--silver-1));
    box-shadow: 0 6px 18px rgba(0,0,0,.18);
  }
  .card--front { top: 129px; height: 452px; }
  .card--back  { top: 679px; height: 443px; }

  .card__inner { position: relative; width: 100%; height: 100%; overflow: hidden;
    background: linear-gradient(180deg, var(--panel-light), var(--panel)); }

  .band {
    position: absolute; left: 0; top: 0; width: 100%;
    background: radial-gradient(ellipse at 50% 40%, var(--band-mid), var(--band-dark) 75%);
    border-bottom: 3px solid var(--silver-2);
  }
  .card--front .band { height: 217px; }
  .card--back .band { height: 208px; }

  .logo { position: absolute; left: 145px; top: 48px; display: flex; align-items: center; gap: 20px; }
  .logo__mark { width: 104px; height: 104px; border-radius: 50%; background: var(--logo-grey); }
  .logo__name { font-family: "Raleway", sans-serif; font-weight: 300; font-size: 34px;
    letter-spacing: 3px; color: var(--logo-grey); text-transform: uppercase; }

  .info { position: absolute; left: 0; width: 100%; height: 160px; }
  .card--front .info { top: 262px; }
  .info__identity { position: absolute; left: 75px; top: 0; }
  .info__name { font-weight: 700; font-size: 22px; color: var(--ink); }
  .info__role { font-size: 16px; color: var(--ink-soft); margin-top: 4px; }
  .info__divider { position: absolute; left: 370px; top: 8px; width: 1px; height: 142px; background: var(--silver-2); }
  .contact { position: absolute; left: 402px; top: 28px; list-style: none; }
  .contact li { display: flex; align-items: center; gap: 14px; font-size: 15px; color: var(--ink); height: 38px; }
  .contact svg { width: 16px; height: 16px; fill: var(--ink); flex: none; }

  .web-line { position: absolute; left: 0; top: 88px; width: 100%; text-align: center;
    color: var(--white); font-size: 24px; letter-spacing: 3px; }
  .web-line strong { font-weight: 700; }

  .info--mirrored { top: 218px; transform: scaleX(-1); opacity: .3; filter: blur(.6px); }
</style>
</head>
<body>

<section class="card card--front">
  <div class="card__inner">
    <div class="band" role="img" aria-label="Dark band with a repeating embossed monogram pattern">
      <div class="logo">
        <span class="logo__mark"></span>
        <span class="logo__name">Marcus Feldwright</span>
      </div>
    </div>
    <div class="info">
      <div class="info__identity">
        <p class="info__name">Marcus Feldwright</p>
        <p class="info__role">Jewellery Stylist</p>
      </div>
      <span class="info__divider"></span>
      <ul class="contact">
        <li><svg viewBox="0 0 16 16"><circle cx="8" cy="8" r="8"/><path d="M5 4h2l1 2-1 1c.6 1.2 1.3 1.9 2.5 2.5l1-1 2 1v2c-4 .5-8-3.5-7.5-7.5z" fill="#dcd7cf"/></svg>0492 836 514</li>
        <li><svg viewBox="0 0 16 16"><path d="M1 3h14v10H1z"/><path d="M1 3l7 6 7-6" fill="none" stroke="#dcd7cf" stroke-width="1.4"/></svg>marcus@marcusfeldwright.com</li>
        <li><svg viewBox="0 0 16 16"><rect x="1" y="11" width="2.5" height="3"/><rect x="5" y="9" width="2.5" height="5"/><rect x="9" y="6" width="2.5" height="8"/><rect x="13" y="3" width="2.5" height="11"/></svg>www.marcusfeldwright.com</li>
      </ul>
    </div>
  </div>
</section>

<section class="card card--back">
  <div class="card__inner">
    <div class="band" role="img" aria-label="Dark band with a repeating embossed monogram pattern">
      <p class="web-line">www.<strong>MarcusFeldwright</strong>.com</p>
    </div>
    <div class="info info--mirrored" aria-hidden="true">
      <div class="info__identity">
        <p class="info__name">Marcus Feldwright</p>
        <p class="info__role">Jewellery Stylist</p>
      </div>
      <ul class="contact">
        <li><svg viewBox="0 0 16 16"><circle cx="8" cy="8" r="8"/></svg>0492 836 514</li>
        <li><svg viewBox="0 0 16 16"><path d="M1 3h14v10H1z"/></svg>marcus@marcusfeldwright.com</li>
        <li><svg viewBox="0 0 16 16"><rect x="1" y="11" width="2.5" height="3"/><rect x="5" y="9" width="2.5" height="5"/><rect x="9" y="6" width="2.5" height="8"/><rect x="13" y="3" width="2.5" height="11"/></svg>www.marcusfeldwright.com</li>
      </ul>
    </div>
  </div>
</section>

</body>
</html>
```